KeyHarbor needs a modern business card

We are a modern conveyancing company and we need to appeal to the top (Multi-million dollar properties)and bottom on the property conveyancing market but our sweet spot is the middle of the market. I like professional with a hint of unconventional.

Target Market(s)

As above

Industry/Entity Type

Real Estate

Contact Information for Business Card

Back Of card:
thinking black with the logo and a tag line (I could be wrong about the black)
Tag line - Right Expertise, Exceptional Service

Front of Card:
Marissa Toll (BBus (Finance) LLB)
Licensed Conveyancer
Email: marissa@keyharbor.com.au

Key Harbor
ABN: 48 913 706
Suite 14, Level 3, 9 Calloway Road Lindhurst Park, NSW 2178
Phone: 1300 682 917

Sydney - Melbourne - Brisbane (Perhaps have this along the bottom of the card)

Requirements
Must have
• Sleek, modern and top end appeal (But approachable)
Should not have
• Not too cluttered

```html
<!DOCTYPE html>
<html lang="en">
<head>
<meta charset="utf-8">
<title>KeyHarbor Business Card</title>
<link rel="stylesheet" href="https://fonts.googleapis.com/css2?family=Roboto:wght@400;500;700&display=swap">
<style>
  :root {
    --backdrop: #a8a6a7;
    --card-dark: #262626;
    --card-light: #f4f4f4;
    --navy: #355a7e;
    --sky: #2196f3;
    --lime: #7cc42a;
    --ink: #2a2a2a;
    --white: #ffffff;
  }
  * { margin: 0; padding: 0; box-sizing: border-box; }
  html, body {
    width: 1200px; height: 1200px; overflow: hidden;
    background: var(--backdrop);
    font-family: "Roboto", Arial, sans-serif;
  }
  .canvas { position: relative; width: 1200px; height: 1200px; }

  /* Back of card */
  .card-back {
    position: absolute; left: 238px; top: 117px;
    width: 713px; height: 420px;
    background: var(--card-dark);
  }
  .card-back .brand {
    position: absolute; left: 0; right: 0; top: 300px;
    display: flex; justify-content: center; align-items: center; gap: 16px;
    color: var(--white); font-size: 44px; font-weight: 500; letter-spacing: -0.5px;
  }
  .brand-square { width: 22px; height: 22px; background: var(--navy); }
  .card-back .tagline {
    position: absolute; left: 0; right: 0; top: 370px;
    display: flex; justify-content: center; align-items: center; gap: 14px;
    color: var(--white); font-size: 18px;
  }
  .rule { display: block; width: 80px; height: 4px; }
  .rule--blue { background: linear-gradient(to right, transparent, var(--sky) 20%); }
  .rule--green { background: linear-gradient(to left, transparent, var(--lime) 20%); }

  /* Front of card */
  .card-front {
    position: absolute; left: 231px; top: 644px;
    width: 711px; height: 416px;
    background: var(--card-light);
    color: var(--ink);
  }
  .side-band { position: absolute; left: 0; top: 0; width: 60px; height: 100%; background: var(--navy); }
  .side-stripe { position: absolute; left: 60px; top: 0; width: 8px; height: 100%; background: var(--lime); }
  .person { position: absolute; left: 94px; top: 62px; }
  .person-name { color: var(--navy); font-size: 30px; font-weight: 700; line-height: 1; }
  .person-title { margin-top: 12px; font-size: 16px; line-height: 21px; }
  .card-front .brand {
    position: absolute; right: 36px; top: 208px;
    display: flex; align-items: center; gap: 14px;
    color: var(--ink); font-size: 38px; font-weight: 500; letter-spacing: -0.5px;
  }
  .contact { position: absolute; left: 94px; top: 292px; font-size: 18px; line-height: 26px; }
  .contact-row { display: flex; align-items: center; gap: 14px; }
  .contact-row svg { width: 18px; height: 14px; }
  .company { position: absolute; left: 399px; top: 292px; font-size: 18px; line-height: 26px; }
  .address { position: absolute; left: 94px; top: 353px; font-size: 18px; }
</style>
</head>
<body>
<div class="canvas">
  <section class="card-back">
    <div class="brand"><span class="brand-square"></span>KeyHarbor</div>
    <div class="tagline">
      <span class="rule rule--blue"></span>
      Right Expertise, Exceptional Service
      <span class="rule rule--green"></span>
    </div>
  </section>

  <section class="card-front">
    <div class="side-band"></div>
    <div class="side-stripe"></div>
    <div class="person">
      <div class="person-name">Marissa Toll</div>
      <div class="person-title">(BBus (Finance) LLB)<br>Licensed Conveyancer</div>
    </div>
    <div class="brand"><span class="brand-square"></span>KeyHarbor</div>
    <div class="contact">
      <div class="contact-row">
        <svg viewBox="0 0 18 14" aria-hidden="true"><path d="M1 5 Q9 -1 17 5 L14 6 L12 4 L6 4 L4 6 Z M4 7 H14 L15 13 H3 Z" fill="#1e7fd1"/></svg>
        1300 682 917
      </div>
      <div class="contact-row">
        <svg viewBox="0 0 18 14" aria-hidden="true"><rect x="1" y="2" width="16" height="10" fill="#7cc42a"/><path d="M1 2 L9 8 L17 2" stroke="#f4f4f4" stroke-width="1.5" fill="none"/></svg>
        marissa@keyharbor.com.au
      </div>
    </div>
    <div class="company">
      <div>ABN: 48 913 706</div>
      <div>Sydney &nbsp;|&nbsp; Melbourne &nbsp;|&nbsp; Brisbane</div>
    </div>
    <div class="address">Suite 14, Level 3, 9 Calloway Road Lindhurst Park, NSW 2178</div>
  </section>
</div>
</body>
</html>
```